swimming pool Leak Detection Brochure

I would Like to create a pool leak detection brochure

Target Market(s)

High end Clients with inground swimming pools

Industry/Entity Type

Pool Service

Font styles to use
Other font styles liked:
• Im open to suggestions but using my website for ideas is suggested

Colors

Designer to choose colors to be used in the design.

Requirements
Must have
• Do you Have a Leak??
• Figuring out when your pool has a leak can be tough. Environmental factors do play a role in the water level, and just because your pool’s water is lower than normal does not mean it has a leak. Wind, humidity, and sun exposure all impact your rate of evaporation.
• Warning Signs of a Leak in Your Pool
• Your pool, fountain, or spa loses more than 1/4 an inch of water a day
• There are cracks in or around the pool decking
• You need to add water more than once a week
• Grass around the area is soggy
• Your pool deck is sinking or lifting
Nice to have
• PREPARING FOR A LEAK TEST
• To ensure you receive an accurate leak detection test, it is required that you have the pool vacuumed and cleaned beforehand. Dirt and debris in the pool can make it difficult to spot even large leaks. Likewise, the water should be as clear as possible. If your water is green it means mildew, algae, or fungi has infested it. Not only does this make it impossible to test for leaks, but it’s dangerous for our health. Finally our pool should be full to the normal level - we can’t find a leak that is not leaking! After your test, you will be confident knowing you have a pool/fountain/spa that is free of leaks or the Leak has been found and can be repaired Properly.

```html
<!DOCTYPE html>
<html lang="en">
<head>
<meta charset="utf-8">
<title>Clearbay Pool Service – Leak Detection Brochure Cover Spread</title>
<link rel="stylesheet" href="https://fonts.googleapis.com/css2?family=Open+Sans:wght@400;600;700;800&family=Playfair+Display:wght@400&display=swap">
<style>
  :root {
    --bg: #3a3d42;
    --navy: #1f4795;
    --deep: #244e9f;
    --royal: #2a5fb7;
    --sky: #4a86cf;
    --light-band: #3f7bc8;
    --white: #ffffff;
    --orange: #e8702a;
    --gold: #f29a2e;
    --photo-pool: #1e6fd0;
    --photo-sky: #9cc6ea;
  }
  * { margin: 0; padding: 0; box-sizing: border-box; }
  html, body { width: 1200px; height: 789px; overflow: hidden; background: var(--bg); }
  .spread {
    position: absolute; left: 60px; top: 15px;
    width: 1080px; height: 759px;
    display: flex;
    box-shadow: 0 10px 30px rgba(0,0,0,.45);
  }
  .page { position: relative; width: 540px; height: 759px; overflow: hidden; font-family: "Open Sans", sans-serif; color: var(--white); }
  .page > svg.shapes { position: absolute; inset: 0; }

  /* back cover */
  .back-cover { background: var(--navy); }
  .testimonial { position: absolute; left: 250px; top: 150px; width: 240px; text-align: right; }
  .testimonial .stars { color: var(--gold); font-size: 17px; letter-spacing: 2px; }
  .testimonial .quote-mark { position: absolute; font-family: "Playfair Display", serif; font-size: 64px; line-height: 1; color: var(--white); }
  .testimonial .open { left: -52px; top: 10px; }
  .testimonial .close { right: -42px; top: 96px; }
  .testimonial p { font-size: 10.5px; line-height: 1.45; margin-top: 4px; }
  .testimonial .author { font-weight: 700; font-size: 12px; margin-top: 10px; margin-right: 6px; }

  .contact { position: absolute; left: 195px; top: 505px; width: 280px; text-align: center; }
  .contact h2 { font-size: 15px; font-weight: 700; letter-spacing: .5px; padding-bottom: 6px; border-bottom: 1px solid rgba(255,255,255,.6); margin: 0 40px 10px; }
  .contact .line { font-size: 13px; line-height: 1.6; }
  .contact .email { display: flex; align-items: center; justify-content: center; gap: 6px; }
  .contact .phone {
    margin: 10px auto 8px; width: 260px; height: 44px; border: 1.5px solid var(--white); border-radius: 22px;
    display: flex; align-items: center; gap: 14px; padding-left: 6px;
    font-size: 25px; font-weight: 700; letter-spacing: .5px;
  }
  .contact .phone .icon { width: 32px; height: 32px; border: 1.5px solid var(--white); border-radius: 50%; display: flex; align-items: center; justify-content: center; }
  .contact .web { display: flex; align-items: center; justify-content: center; gap: 6px; font-size: 13px; }
  .url b { font-weight: 700; }

  /* front cover */
  .front-cover { background: var(--light-band); }
  .brand-seal {
    position: absolute; left: 370px; top: 296px; width: 164px; height: 164px; border-radius: 50%;
    background: var(--white); border: 5px solid var(--orange);
    box-shadow: 0 0 0 4px var(--white), 0 4px 10px rgba(0,0,0,.3);
    display: flex; flex-direction: column; align-items: center; justify-content: center; text-align: center; gap: 8px;
  }
  .brand-seal .brand-name { font-weight: 700; font-size: 20px; line-height: 1.1; color: var(--navy); }
  .brand-seal .specialty { font-weight: 700; font-size: 10.5px; line-height: 1.25; letter-spacing: .3px; color: var(--navy); border-top: 1px solid var(--navy); padding-top: 5px; }
  .headline { position: absolute; left: 60px; top: 560px; font-family: "Playfair Display", serif; font-weight: 400; font-size: 29px; line-height: 1.32; }
  .headline span { display: block; }
  .headline span:nth-child(2) { padding-left: 14px; }
  .headline span:nth-child(3) { padding-left: 28px; }
  .front-web { position: absolute; right: 30px; top: 535px; font-size: 14px; padding-bottom: 5px; border-bottom: 2px solid var(--orange); }
</style>
</head>
<body>
<main class="spread">

  <!-- Back cover -->
  <section class="page back-cover">
    <svg class="shapes" width="540" height="759" viewBox="0 0 540 759">
      <defs>
        <linearGradient id="skimmerPhoto" x1="0" y1="0" x2="1" y2="1">
          <stop offset="0" stop-color="#eef1f4"/>
          <stop offset=".28" stop-color="#c9d3de"/>
          <stop offset=".36" stop-color="#2f62c0"/>
          <stop offset="1" stop-color="#2650a8"/>
        </linearGradient>
      </defs>
      <rect role="img" aria-label="Photo of a pool skimmer net cleaning a tiled blue pool edge" width="540" height="560" fill="url(#skimmerPhoto)"/>
      <path d="M0 560 C 120 420, 320 380, 540 400 L540 759 L0 759 Z" fill="var(--deep)"/>
      <path d="M0 575 C 120 440, 320 395, 540 415" fill="none" stroke="#6fa3e0" stroke-width="1.5"/>
      <circle cx="85" cy="565" r="52" fill="#e9edf2" stroke="#ffffff" stroke-width="4"/>
      <circle cx="85" cy="565" r="56" fill="none" stroke="var(--orange)" stroke-width="2"/>
      <circle cx="85" cy="570" r="28" fill="#24437f"/>
      <circle cx="215" cy="465" r="50" fill="#e9edf2" stroke="#ffffff" stroke-width="4"/>
      <circle cx="215" cy="465" r="54" fill="none" stroke="var(--orange)" stroke-width="2"/>
      <circle cx="215" cy="465" r="30" fill="#3b79c6"/>
      <circle cx="345" cy="420" r="44" fill="#e9edf2" stroke="#ffffff" stroke-width="4"/>
      <circle cx="345" cy="420" r="48" fill="none" stroke="var(--orange)" stroke-width="2"/>
      <circle cx="345" cy="420" r="27" fill="#2a5fb7"/>
    </svg>

    <div class="testimonial">
      <span class="quote-mark open">“</span>
      <div class="stars">★★★★★</div>
      <p>I am so happy I found this company A1 service! I highly recommend this company..my pool was green all last summer with another company.. Clearbay pool service came in and with in 3 days my pool turned around.. We are beyond happy..</p>
      <div class="author">Marcus T.</div>
      <span class="quote-mark close">”</span>
    </div>

    <div class="contact">
      <h2>CONTACT US</h2>
      <div class="line">Clearbay Pool Service</div>
      <div class="line">RI REG # 40917</div>
      <div class="line">CT License # SP1- PLM 0571326</div>
      <div class="line email">
        <svg width="14" height="10" viewBox="0 0 14 10"><rect x=".5" y=".5" width="13" height="9" fill="none" stroke="#fff"/><path d="M.5 .5 L7 6 L13.5 .5" fill="none" stroke="#fff"/></svg>
        <span>hello@clearbaypools.com</span>
      </div>
      <div class="phone">
        <span class="icon"><svg width="16" height="16" viewBox="0 0 24 24"><path d="M6.6 10.8a15 15 0 0 0 6.6 6.6l2.2-2.2a1 1 0 0 1 1-.25 11.4 11.4 0 0 0 3.6.57 1 1 0 0 1 1 1V20a1 1 0 0 1-1 1A17 17 0 0 1 3 4a1 1 0 0 1 1-1h3.5a1 1 0 0 1 1 1c0 1.25.2 2.45.57 3.57a1 1 0 0 1-.25 1z" fill="#fff"/></svg></span>
        <span>555-014-2290</span>
      </div>
      <div class="web">
        <svg width="13" height="13" viewBox="0 0 14 14"><circle cx="7" cy="7" r="6" fill="none" stroke="#fff"/><ellipse cx="7" cy="7" rx="2.6" ry="6" fill="none" stroke="#fff"/><path d="M1 7h12" stroke="#fff"/></svg>
        <span class="url">www.<b>clearbaypools</b>.com</span>
      </div>
    </div>
  </section>

  <!-- Front cover -->
  <section class="page front-cover">
    <svg class="shapes" width="540" height="759" viewBox="0 0 540 759">
      <defs>
        <linearGradient id="resortPhoto" x1="0" y1="0" x2="0" y2="1">
          <stop offset="0" stop-color="var(--photo-sky)"/>
          <stop offset=".25" stop-color="#6e9f73"/>
          <stop offset=".42" stop-color="#3d83d8"/>
          <stop offset="1" stop-color="var(--photo-pool)"/>
        </linearGradient>
      </defs>
      <path role="img" aria-label="Photo of a resort swimming pool with palm trees and swimmers" d="M0 0 H540 V400 C 430 470, 250 490, 0 430 Z" fill="url(#resortPhoto)"/>
      <path d="M0 438 C 250 498, 430 478, 540 408" fill="none" stroke="#9cc4f0" stroke-width="2"/>
      <path d="M0 450 C 250 515, 430 495, 540 425 V759 H0 Z" fill="var(--sky)" opacity=".5"/>
    </svg>

    <div class="brand-seal">
      <span class="brand-name">Clearbay</span>
      <span class="specialty">LEAK DETECTION<br>SPECIALIST</span>
    </div>
    <div class="front-web url">www.<b>clearbaypools</b>.com</div>
    <h1 class="headline">
      <span>Dive Into</span>
      <span>Professional Pool</span>
      <span>Service &amp; Repair</span>
    </h1>
  </section>

</main>
</body>
</html>
```